Build a Web page - Dovin Pratchell Homes, LLC - a custom home builder

We are a custom home builder in Wisconsin. Need a basic web page with a home page, About Us, Contact info, Gallery, and Testimonials page. Gallery will probably have sub-pages and each will have about ten pictures or less. I already own the domain and have web hosting through Wix, I just need the site built. Once the page is built I should be able to do the upkeep on it myself. If I need to add pictures or whatever.
Updates

Project Deadline Extended
Reason: I am still looking through designs and will select soon - thank you!

Target Market(s)

Gen X and Millennials who are looking to build a home. Custom built homes - not generic spec homes.

Industry/Entity Type

Home Builder

Number of Pages Required

5+ page

Font styles to use
Sans Serif

Colors
ffffff
ec1f27
000000
9d9d9d

Requirements
Must have
• I have no idea if I want coded or in coded. I'm not sure of the difference and why I would want one over the other.
Nice to have
• We like the following colors - red, black, gray, white.
Should not have
• not a big fan of clip art like hammers, tape measures, etc. Must look professional.

```html
<!DOCTYPE html>
<html lang="en">
<head>
<meta charset="utf-8">
<title>Dovin Pratchell Homes — Custom Home Builder</title>
<link href="https://fonts.googleapis.com/css2?family=Open+Sans:wght@400;600;700;800&display=swap" rel="stylesheet">
<style>
:root{
  --red:#ec1f27;
  --black:#000000;
  --ink:#222222;
  --text:#555555;
  --grey:#9d9d9d;
  --band:#ebebed;
  --footer:#3a3a3a;
  --white:#ffffff;
}
*{margin:0;padding:0;box-sizing:border-box}
html,body{width:1200px;height:2917px;overflow:hidden}
body{position:relative;font-family:"Open Sans",Arial,sans-serif;background:var(--white);color:var(--ink)}
.abs{position:absolute}

/* hero */
.hero{left:0;top:0;width:1200px;height:705px;
  background:linear-gradient(180deg,#5c87c9 0%,#9fbbe0 28%,#8a8f7e 48%,#6f7c5a 62%,#5d8a32 78%,#8d8e88 100%)}
.nav{right:0;top:0;height:40px;display:flex;align-items:center;background:rgba(255,255,255,.95);padding-right:22px}
.nav a{display:block;height:40px;line-height:40px;padding:0 18px;font-size:11px;font-weight:600;color:var(--ink);text-decoration:none;text-transform:uppercase}
.nav a.active{background:var(--red);color:var(--white)}
.nav .phone{display:flex;align-items:center;gap:6px;color:var(--red);font-weight:700;font-size:17px;margin-left:6px}
.brand{width:150px;height:135px;background:var(--white);border:3px solid #cfcfcf;display:flex;flex-direction:column;align-items:center;justify-content:center;gap:8px;text-align:center}
.brand .mark{width:14px;height:14px;background:var(--red)}
.brand span{font-size:15px;font-weight:700;color:var(--ink);line-height:1.2}
.hero-title{left:142px;top:525px;font-size:52px;font-weight:800;line-height:1.0;color:var(--white);text-transform:uppercase}
.arrow{width:30px;height:30px;background:var(--white);display:flex;align-items:center;justify-content:center}

/* welcome */
.welcome{left:130px;top:792px;width:936px;height:340px;border:3px solid #8a8a8a}
.welcome h2{left:40px;top:-19px;background:var(--white);padding:0 12px;color:var(--red);font-size:26px;font-weight:800;text-transform:uppercase}
.welcome .lead{left:50px;top:50px;width:410px;font-size:14px;line-height:1.55;color:var(--ink)}
.welcome .body{left:50px;top:110px;width:380px;font-size:12.5px;line-height:1.55;color:var(--text)}
.btn{display:flex;align-items:center;justify-content:center;background:var(--red);color:var(--white);font-size:12px;font-weight:700;text-transform:uppercase}
.welcome .btn{left:52px;top:252px;width:122px;height:36px}
.welcome .photo{right:0;top:46px;width:443px;height:291px;background:linear-gradient(180deg,#e6ebf0 0%,#cfd4da 40%,#9c9a8e 70%,#3f7d2a 100%)}

/* services */
.services{left:0;top:1203px;width:1200px;height:532px;background:var(--band)}
.section-title{width:1200px;text-align:center;color:var(--red);font-size:26px;font-weight:800;text-transform:uppercase}
.service{top:172px;width:258px;text-align:center}
.service + .service{border-left:1px solid #d6d6d6}
.service svg{display:block;margin:0 auto 22px}
.service h3{font-size:15px;font-weight:700;color:var(--black);margin-bottom:16px}
.service p{font-size:12px;line-height:1.6;color:var(--text);padding:0 28px}
.services .btn{left:542px;top:437px;width:122px;height:36px}

/* gallery */
.gallery{left:143px;top:1875px;width:923px;display:grid;grid-template-columns:repeat(4,1fr);gap:3px}
.tile{border:1px solid #dcdcdc;background:var(--white)}
.tile .shot{height:167px}
.tile p{height:40px;line-height:40px;text-align:center;font-size:12.5px;color:var(--ink)}

/* call */
.call{left:0;top:2375px;width:1200px;height:158px;background:var(--red)}
.call .person{left:205px;top:-42px;width:190px;height:200px;background:linear-gradient(180deg,#c89a78 0%,#8a5b44 40%,#1f55b8 70%,#1a4aa3 100%);border-radius:95px 95px 0 0}
.call h2{left:484px;top:40px;font-size:38px;font-weight:800;color:var(--white)}
.call p{left:488px;top:96px;font-size:19px;color:var(--white);text-transform:uppercase}

/* footer */
.footer{left:0;top:2533px;width:1200px;height:384px;background:var(--footer);color:var(--white)}
.footer .brand{left:133px;top:64px;width:148px;height:135px}
.footer h4{font-size:13px;font-weight:700;text-transform:uppercase}
.menu{left:345px;top:96px;display:flex;font-size:12px}
.menu span{padding:0 9px;border-left:1px solid #888}
.menu span:first-child{padding-left:0;border-left:0}
.social{left:347px;top:175px;display:flex;gap:9px}
.social i{width:30px;height:30px;border-radius:50%;display:block}
.email{left:780px;top:95px;width:288px;height:47px;background:#2c2c2c;display:flex;align-items:center;gap:14px;padding-left:20px;font-size:12px;color:#ddd}
.footer .btn{left:783px;top:161px;width:123px;height:46px;font-size:15px}
.rule{left:133px;top:275px;width:934px;height:1px;background:#555}
.copy{width:1200px;top:322px;text-align:center;font-size:12px;color:var(--grey)}
</style>
</head>
<body>

<header class="abs hero" role="img" aria-label="Photo of a two-storey custom home with stone garage front and green lawn under a blue sky">
  <nav class="abs nav">
    <a class="active">Home</a><a>About Us</a><a>Gallery</a><a>Testimonials</a><a>Contact Us</a>
    <span class="phone">
      <svg width="16" height="16" viewBox="0 0 16 16"><rect width="16" height="16" fill="#ec1f27"/><path d="M5 3.5l2 2-1.2 1.3a6 6 0 003.4 3.4L10.5 9l2 2-1.3 1.5C7.5 12.5 3.5 8.5 3.5 4.8z" fill="#fff"/></svg>
      555.010.4477
    </span>
  </nav>
  <div class="abs brand" style="left:133px;top:20px"><i class="mark"></i><span>Dovin Pratchell<br>Homes</span></div>
  <h1 class="abs hero-title">Custom<br>Home Builder</h1>
  <div class="abs arrow" style="left:998px;top:585px"><svg width="10" height="10" viewBox="0 0 10 10"><path d="M7 1L2 5l5 4z" fill="#222"/></svg></div>
  <div class="abs arrow" style="left:1038px;top:585px"><svg width="10" height="10" viewBox="0 0 10 10"><path d="M3 1l5 4-5 4z" fill="#222"/></svg></div>
</header>

<section class="abs welcome">
  <h2 class="abs">Welcome to Our Site</h2>
  <p class="abs lead">Lorem Ipsum is simply dummy text of the printing and typesetting industry. Lorem Ipsum has been the</p>
  <p class="abs body">There are many variations of passages of Lorem Ipsum available, but the majority have suffered alteration in some form, by injected humour, or randomised words which don't look even slightly believable. If you are going to use a passage of Lorem Ipsum, you need to be sure there isn't anything embarrassing hidden in the middle of text.</p>
  <a class="abs btn">Read More</a>
  <div class="abs photo" role="img" aria-label="Photo of a beige two-storey house with a front porch and lawn"></div>
</section>

<section class="abs services">
  <h2 class="abs section-title" style="top:80px">Our Services</h2>
  <div class="abs service" style="left:140px">
    <svg width="66" height="56" viewBox="0 0 66 56"><rect x="8" y="6" width="50" height="44" fill="none" stroke="#ec1f27" stroke-width="5"/><path d="M18 16h30M18 26h20M18 36h30" stroke="#ec1f27" stroke-width="4"/></svg>
    <h3>Create Wireframe</h3>
    <p>There are many variations of passages of Lorem Ipsum available, but the majority have suffered</p>
  </div>
  <div class="abs service" style="left:398px">
    <svg width="76" height="56" viewBox="0 0 76 56"><path d="M38 4L6 30h10v20h44V30h10z" fill="#ec1f27"/><rect x="32" y="32" width="12" height="18" fill="#ebebed"/><path d="M2 52h72" stroke="#ec1f27" stroke-width="4"/></svg>
    <h3>Selection Design</h3>
    <p>There are many variations of passages of Lorem Ipsum available, but the majority have suffered</p>
  </div>
  <div class="abs service" style="left:656px">
    <svg width="56" height="56" viewBox="0 0 56 56"><circle cx="28" cy="28" r="24" fill="none" stroke="#ec1f27" stroke-width="4"/><text x="28" y="39" text-anchor="middle" font-family="Open Sans, sans-serif" font-weight="700" font-size="30" fill="#ec1f27">$</text></svg>
    <h3>Financing</h3>
    <p>There are many variations of passages of Lorem Ipsum available, but the majority have suffered</p>
  </div>
  <div class="abs service" style="left:914px">
    <svg width="50" height="56" viewBox="0 0 50 56"><path d="M4 54V6h14v8h14V6h14v48z" fill="#ec1f27"/><path d="M11 20h6M11 30h6M11 40h6M33 20h6M33 30h6M33 40h6M22 24h6M22 34h6" stroke="#ebebed" stroke-width="4"/></svg>
    <h3>Custom Building</h3>
    <p>There are many variations of passages of Lorem Ipsum available, but the majority have suffered</p>
  </div>
  <a class="abs btn">Read More</a>
</section>

<h2 class="abs section-title" style="top:1792px;left:0">Photo Gallery</h2>
<section class="abs gallery">
  <figure class="tile"><div class="shot" role="img" aria-label="Living room with fireplace" style="background:linear-gradient(160deg,#c9b69a,#7a4a3a)"></div><p>Heading 1</p></figure>
  <figure class="tile"><div class="shot" role="img" aria-label="Wooden staircase" style="background:linear-gradient(160deg,#e4ddd0,#8a4e2c)"></div><p>Heading 2</p></figure>
  <figure class="tile"><div class="shot" role="img" aria-label="Bedroom with patterned quilt" style="background:linear-gradient(160deg,#6b4a3a,#a8343a)"></div><p>Heading 3</p></figure>
  <figure class="tile"><div class="shot" role="img" aria-label="Family room with built-in shelves" style="background:linear-gradient(160deg,#d8cbb4,#6e5040)"></div><p>Heading 4</p></figure>
  <figure class="tile"><div class="shot" role="img" aria-label="Backyard patio and lawn" style="background:linear-gradient(180deg,#d7dfe6,#8b8a80 50%,#4f8a30)"></div><p>Heading 5</p></figure>
  <figure class="tile"><div class="shot" role="img" aria-label="Hallway with wood floor" style="background:linear-gradient(180deg,#e7e4de,#9a7048)"></div><p>Heading 6</p></figure>
  <figure class="tile"><div class="shot" role="img" aria-label="Wooden deck behind a house" style="background:linear-gradient(180deg,#cfd2d0,#8b5048)"></div><p>Heading 7</p></figure>
  <figure class="tile"><div class="shot" role="img" aria-label="Television over a fireplace mantel" style="background:linear-gradient(160deg,#c99a40,#3a2e28)"></div><p>Heading 8</p></figure>
</section>

<section class="abs call">
  <div class="abs person" role="img" aria-label="Customer service representative with headset"></div>
  <h2 class="abs">CALL TODAY! +1 555-014-2290</h2>
  <p class="abs">For a free consultation</p>
</section>

<footer class="abs footer">
  <div class="abs brand"><i class="mark"></i><span>Dovin Pratchell<br>Homes</span></div>
  <h4 class="abs" style="left:345px;top:64px">Menu</h4>
  <div class="abs menu"><span>Home</span><span>About us</span><span>Gallery</span><span>Testimonials</span><span>Contact us</span></div>
  <h4 class="abs" style="left:347px;top:145px">Follow us on</h4>
  <div class="abs social"><i style="background:#3b5bb5"></i><i style="background:#1da1e0"></i><i style="background:#e0503a"></i></div>
  <h4 class="abs" style="left:780px;top:64px">Newsletter</h4>
  <div class="abs email">
    <svg width="12" height="10" viewBox="0 0 12 10"><rect x=".5" y=".5" width="11" height="9" fill="none" stroke="#ccc"/><path d="M.5 .5L6 5l5.5-4.5" fill="none" stroke="#ccc"/></svg>
    E mail id
  </div>
  <a class="abs btn">Signup</a>
  <div class="abs rule"></div>
  <p class="abs copy">Copyrights © 2017 All Rights Reserved</p>
</footer>

</body>
</html>
```